Website for IT consulting Company

I need a website upgrade, the existing site content is ok, I would also like to add a testimonial page, the site should be something that is easy for us to update content. You use the content from www.velmarketa.com as an example. I will also post update logo and artwork. I also need a contact form with some type of validation or captcha.

Please omit Address maps

Target Market(s)

small business, service oriented companies. We provide IT Consulting, support and mangement

Industry/Entity Type

Information Technology

Coding

Coded - Design and coding required

Number of Pages Required

1 page

Font styles to use
Serif
Sans Serif

Requirements
Must have
• Contain logo attached, and content from existing web site www.velmarketa.com.
• Also need to update content easily, and be movable to different platforms.
• There is a catch phrase
• "Let us worry about your technology…” “ so you don’t have to!”
• Should be included.
Nice to have
• Testimonial page, Project page where we can post new and past projects and pictures
Should not have
• none

```html
<!DOCTYPE html>
<html lang="en">
<head>
<meta charset="utf-8">
<title>Velmarketa — IT Consulting</title>
<link rel="stylesheet" href="https://fonts.googleapis.com/css2?family=Roboto:wght@300;400;500;700&display=swap">
<style>
:root{
  --orange:#f0862e;
  --orange-soft:#fde6d2;
  --blue:#1e9ad6;
  --lime:#b4c22b;
  --ink:#2a2a2a;
  --muted:#6b6b6b;
  --line:#d8d8d8;
  --panel:#f4f4f4;
  --footer:#232228;
  --white:#ffffff;
}
*{box-sizing:border-box;margin:0;padding:0}
html,body{width:1200px;height:2908px;overflow:hidden}
body{position:relative;font-family:"Roboto",Arial,sans-serif;color:var(--ink);background:var(--white)}
.abs{position:absolute}

/* hero */
.hero{left:0;top:0;width:1200px;height:620px;background:linear-gradient(180deg,#9b9b98 0%,#c9c9c6 45%,#a9a9a6 100%)}
.hero-photo{left:0;top:0;width:1200px;height:620px;background:radial-gradient(ellipse at 50% 40%,rgba(240,240,238,.55),rgba(110,110,108,.35) 75%)}
.hero-shade{left:0;top:0;width:1200px;height:620px;background:rgba(40,40,40,.28)}
.brand{display:flex;align-items:center;gap:10px;font-weight:700;letter-spacing:1px;color:var(--white)}
.brand-mark{width:26px;height:26px;background:var(--orange)}
.hero .brand{left:87px;top:14px;font-size:30px}
.nav{right:72px;top:22px;display:flex;gap:34px;font-size:14px;color:var(--white)}
.nav-rule{left:87px;top:64px;width:1026px;height:1px;background:rgba(255,255,255,.35)}
.hero-title{left:0;width:1200px;top:272px;text-align:center;color:var(--white);font-size:52px;font-weight:500;letter-spacing:-.5px}
.hero-sub{left:0;width:1200px;top:330px;text-align:center;color:var(--white);font-size:17px}
.btn{display:flex;align-items:center;justify-content:center;font-size:13px;background:var(--orange);color:var(--white);border-radius:2px}
.hero .btn{left:522px;top:366px;width:156px;height:34px}
.slide-count{left:1138px;top:270px;width:30px;text-align:center;color:var(--white);font-size:16px}
.notch{left:585px;top:602px}

/* intro */
.intro-frame-h{left:87px;top:683px;width:284px;height:3px;background:var(--orange)}
.intro-frame-v{left:87px;top:683px;width:3px;height:290px;background:var(--orange)}
.intro-photo{left:99px;top:700px;width:446px;height:297px;background:linear-gradient(135deg,#e9eef2,#c9d2d9 55%,#8e5a4f)}
.intro-text{left:582px;top:748px;width:540px}
.intro-head{border-left:3px solid var(--orange);padding-left:20px;margin-bottom:20px}
.eyebrow{font-size:13px;color:var(--muted);line-height:18px}
.intro-title{font-size:25px;font-weight:400;line-height:34px;white-space:nowrap}
.intro-body{font-size:13px;line-height:20px;color:var(--muted);margin-bottom:22px}
.btn-soft{width:122px;height:33px;background:var(--orange-soft);color:var(--orange);font-size:13px;display:flex;align-items:center;justify-content:center}

/* services */
.services{left:0;top:1066px;width:1200px;height:437px;background:var(--panel)}
.section-title{font-size:27px;font-weight:400;text-align:center}
.section-title::after{content:"";display:block;width:40px;height:3px;background:var(--orange);margin:12px auto 0}
.services .section-title{left:0;width:1200px;top:52px}
.card{top:123px;width:287px;height:252px;color:var(--white);padding:44px 18px 0 32px}
.card svg{display:block;margin-bottom:14px}
.card h3{font-size:15.5px;font-weight:400;margin-bottom:16px;line-height:18px;min-height:18px}
.card p{font-size:12.5px;line-height:20px;margin-bottom:14px}
.card .more{font-size:13px}
.card-orange{left:143px;background:var(--orange)}
.card-blue{left:457px;background:var(--blue)}
.card-lime{left:772px;background:var(--lime)}

/* it support */
.support-title{left:237px;top:1646px;font-size:27px;font-weight:400}
.checklist{list-style:none;font-size:12px;color:var(--muted);text-transform:uppercase}
.checklist li{height:31px;display:flex;align-items:center;gap:9px}
.col-a{left:238px;top:1710px}
.col-b{left:477px;top:1710px}
.device{left:717px;top:1567px;width:483px;height:376px;background:linear-gradient(180deg,#2b2b2b 0%,#1c1c1c 92%,#9a9a9a 93%,#c8c8c8 100%);border-radius:16px 0 0 6px}
.device-screen{left:742px;top:1590px;width:458px;height:335px;background:var(--white);display:flex;align-items:center;justify-content:center;font-size:38px;font-weight:700;color:#7a7a7a;letter-spacing:1px}

/* contact */
.contact{left:0;top:2003px;width:1200px;height:533px;background:var(--panel)}
.contact-photo{left:89px;top:66px;width:314px;height:405px;background:linear-gradient(160deg,#9fb3c4,#6d7d8a 50%,#3a3f45)}
.form-card{left:423px;top:66px;width:686px;height:405px;background:var(--white);box-shadow:0 2px 14px rgba(0,0,0,.06)}
.form-title{left:53px;top:38px;font-size:17px;font-weight:500}
.field{width:265px;height:40px;border-bottom:1px solid var(--line);font-size:12px;color:var(--muted);padding-top:10px}
.f1{left:53px;top:83px}.f2{left:350px;top:83px}
.f3{left:53px;top:137px}.f4{left:350px;top:137px}
.f5{left:53px;top:190px;width:562px;height:72px}
.captcha-note{left:56px;top:272px;font-size:12px;color:var(--muted)}
.captcha{left:51px;top:300px;width:270px;height:66px;border:1px solid var(--line);border-radius:3px;background:#f9f9f9;display:flex;align-items:center;padding-left:14px;gap:12px;font-size:13px}
.captcha .box{width:26px;height:26px;border:2px solid #c1c1c1;background:var(--white);border-radius:2px}
.captcha .seal{position:absolute;right:16px;top:16px;width:30px;height:30px;background:#c9d6ea;border-radius:4px}
.form-card .btn{left:335px;top:315px;width:130px;height:36px}

/* footer */
.footer{left:0;top:2536px;width:1200px;height:372px;background:var(--footer);color:#c9c9c9}
.footer .brand{left:89px;top:56px;font-size:30px}
.footer-about{left:89px;top:124px;width:300px;font-size:12.5px;line-height:22px;color:#d6d6d6}
.footer-more{left:89px;top:194px;font-size:13px;color:var(--white)}
.socials{left:89px;top:234px;display:flex;gap:10px}
.socials span{width:30px;height:30px;border-radius:50%;background:#3a3a40;display:block}
.socials span:first-child{background:var(--orange)}
.fcol h4{font-size:15px;font-weight:400;color:var(--white);margin-bottom:20px}
.fcol ul{list-style:none;font-size:12.5px}
.fcol li{height:27px}
.fcol li::before{content:"· ";color:var(--orange)}
.fc1{left:458px;top:62px}.fc2{left:640px;top:62px}.fc3{left:946px;top:62px}
.fc3 li::before{content:none}
.fc3 li{display:flex;gap:10px;line-height:22px;height:auto;margin-bottom:10px}
.copyright{left:0;width:1200px;top:337px;text-align:center;font-size:12px;color:#d6d6d6}
.to-top{left:1139px;top:298px;width:34px;height:34px;border-radius:50%;background:var(--orange)}
</style>
</head>
<body>

<section class="hero abs">
  <div class="hero-photo abs" role="img" aria-label="Photo of a bearded man in glasses working at a desktop computer in a bright office"></div>
  <div class="hero-shade abs"></div>
  <div class="brand abs"><span class="brand-mark"></span>VELMARKETA</div>
  <nav class="nav abs">
    <svg width="14" height="14" viewBox="0 0 14 14"><path d="M1 7 7 1l6 6h-2v6H8V9H6v4H3V7z" fill="#fff"/></svg>
    <span>Contact</span><span>Project</span><span>Support</span><span>Testimonial</span><span>Clients</span><span>Careers</span>
  </nav>
  <div class="nav-rule abs"></div>
  <h1 class="hero-title abs">LET US WORRY</h1>
  <p class="hero-sub abs">About Your Technology So You Don't Have To!</p>
  <a class="btn abs">Get Started With Us</a>
  <div class="slide-count abs">
    <svg width="14" height="20" viewBox="0 0 14 20"><path d="M7 19V2M2 7l5-5 5 5" stroke="#fff" fill="none" stroke-width="1.5"/></svg>
    <div style="margin:6px 0">01</div>
    <svg width="14" height="20" viewBox="0 0 14 20"><path d="M7 1v17M2 13l5 5 5-5" stroke="#fff" fill="none" stroke-width="1.5"/></svg>
  </div>
  <svg class="notch abs" width="30" height="18" viewBox="0 0 30 18"><path d="M0 18 15 0l15 18z" fill="#fff"/><path d="M15 8v6M12 11l3 3 3-3" stroke="#777" fill="none"/></svg>
</section>

<div class="intro-frame-h abs"></div>
<div class="intro-frame-v abs"></div>
<div class="intro-photo abs" role="img" aria-label="Photo of a smiling young man in a plaid shirt typing on a laptop"></div>
<div class="intro-text abs">
  <div class="intro-head">
    <p class="eyebrow">Our Introduction</p>
    <h2 class="intro-title">Flexible Solutions For Your Business Needs</h2>
  </div>
  <p class="intro-body">Velmarketa is a technology solution provider based in Houston, Texas. Our goal is to make technology a non-issue for individuals and small to medium size businesses ranging from 5 to 150 Users. Velmarketa has the experience, the tools, high-level technology solutions and training to power your business and your work force....</p>
  <a class="btn-soft">Read More</a>
</div>

<section class="services abs">
  <h2 class="section-title abs">Our Services</h2>
  <article class="card card-orange abs">
    <svg width="40" height="44" viewBox="0 0 40 44" fill="none" stroke="#fff" stroke-width="2"><path d="M8 2v40M20 2v40M32 2v40"/><rect x="4" y="10" width="8" height="6" fill="#f0862e"/><rect x="16" y="26" width="8" height="6" fill="#f0862e"/><rect x="28" y="14" width="8" height="6" fill="#f0862e"/></svg>
    <h3>Managed IT Solutions</h3>
    <p>Our staff will design, service, administer and maintain your IT needs. We are well versed on all major operating...</p>
    <span class="more">Read More →</span>
  </article>
  <article class="card card-blue abs">
    <svg width="44" height="44" viewBox="0 0 44 44" fill="none" stroke="#fff" stroke-width="2"><rect x="7" y="10" width="30" height="20"/><path d="M2 34h40"/></svg>
    <h3>Remote Diagnostic and Support</h3>
    <p>Do you need a quick solution to a technical problem? With our live remote-assistance tool, a member of our support...</p>
    <span class="more">Read More →</span>
  </article>
  <article class="card card-lime abs">
    <svg width="40" height="44" viewBox="0 0 40 44" fill="none" stroke="#fff" stroke-width="2"><rect x="10" y="14" width="20" height="28" rx="10"/><path d="M20 14v10M20 14C20 6 12 8 12 2"/></svg>
    <h3>IT Infrastructure Design and Installation</h3>
    <p>Do you have more than one site? Do you need remote access? We can design and implement LANS/WANS...</p>
    <span class="more">Read More →</span>
  </article>
</section>

<h2 class="support-title abs">IT Support Solutions</h2>
<ul class="checklist col-a abs">
  <li><svg width="13" height="13" viewBox="0 0 13 13" fill="none" stroke="#f0862e" stroke-width="1.6"><circle cx="6.5" cy="6.5" r="5.5"/><path d="M3.8 6.6l2 2 3.6-3.8"/></svg>Network Administration.</li>
  <li><svg width="13" height="13" viewBox="0 0 13 13" fill="none" stroke="#f0862e" stroke-width="1.6"><circle cx="6.5" cy="6.5" r="5.5"/><path d="M3.8 6.6l2 2 3.6-3.8"/></svg>Desktop Support.</li>
  <li><svg width="13" height="13" viewBox="0 0 13 13" fill="none" stroke="#f0862e" stroke-width="1.6"><circle cx="6.5" cy="6.5" r="5.5"/><path d="M3.8 6.6l2 2 3.6-3.8"/></svg>Telecommunications.</li>
  <li><svg width="13" height="13" viewBox="0 0 13 13" fill="none" stroke="#f0862e" stroke-width="1.6"><circle cx="6.5" cy="6.5" r="5.5"/><path d="M3.8 6.6l2 2 3.6-3.8"/></svg>Disaster Recovery.</li>
  <li><svg width="13" height="13" viewBox="0 0 13 13" fill="none" stroke="#f0862e" stroke-width="1.6"><circle cx="6.5" cy="6.5" r="5.5"/><path d="M3.8 6.6l2 2 3.6-3.8"/></svg>Audio/Video Multimedia.</li>
</ul>
<ul class="checklist col-b abs">
  <li><svg width="13" height="13" viewBox="0 0 13 13" fill="none" stroke="#f0862e" stroke-width="1.6"><circle cx="6.5" cy="6.5" r="5.5"/><path d="M3.8 6.6l2 2 3.6-3.8"/></svg>Web Design.</li>
  <li><svg width="13" height="13" viewBox="0 0 13 13" fill="none" stroke="#f0862e" stroke-width="1.6"><circle cx="6.5" cy="6.5" r="5.5"/><path d="M3.8 6.6l2 2 3.6-3.8"/></svg>Network Cabling.</li>
  <li><svg width="13" height="13" viewBox="0 0 13 13" fill="none" stroke="#f0862e" stroke-width="1.6"><circle cx="6.5" cy="6.5" r="5.5"/><path d="M3.8 6.6l2 2 3.6-3.8"/></svg>Wireless Networks.</li>
  <li><svg width="13" height="13" viewBox="0 0 13 13" fill="none" stroke="#f0862e" stroke-width="1.6"><circle cx="6.5" cy="6.5" r="5.5"/><path d="M3.8 6.6l2 2 3.6-3.8"/></svg>Antivirus Solutions.</li>
  <li><svg width="13" height="13" viewBox="0 0 13 13" fill="none" stroke="#f0862e" stroke-width="1.6"><circle cx="6.5" cy="6.5" r="5.5"/><path d="M3.8 6.6l2 2 3.6-3.8"/></svg>Network Security.</li>
</ul>
<div class="device abs" role="img" aria-label="Laptop showing the company's home screen"></div>
<div class="device-screen abs">VELMARKETA</div>

<section class="contact abs">
  <div class="contact-photo abs" role="img" aria-label="Photo of two businessmen reviewing work on a laptop in a glass-walled office"></div>
  <form class="form-card abs">
    <h3 class="form-title abs">Contact Us</h3>
    <div class="field f1 abs">First Name*</div>
    <div class="field f2 abs">Second Name*</div>
    <div class="field f3 abs">Your Email*</div>
    <div class="field f4 abs">Subject*</div>
    <div class="field f5 abs">Message*</div>
    <p class="captcha-note abs">Please Type The Letters And Numbers Shown In The Image</p>
    <div class="captcha abs"><span class="box"></span>I'm not a robot<span class="seal"></span></div>
    <a class="btn abs">Send Message</a>
  </form>
</section>

<footer class="footer abs">
  <div class="brand abs"><span class="brand-mark"></span>VELMARKETA</div>
  <p class="footer-about abs">Outsourcing is subcontracting a process, such as product design or manufacturing, to a third-party company [1] The decision ...</p>
  <a class="footer-more abs">Read More →</a>
  <div class="socials abs"><span></span><span></span><span></span><span></span></div>
  <div class="fcol fc1 abs"><h4>QuickLinks</h4>
    <ul><li>Home</li><li>Contact</li><li>Project</li><li>Support</li><li>Testimonial</li><li>Clients</li><li>Careers</li></ul></div>
  <div class="fcol fc2 abs"><h4>Our Services</h4>
    <ul><li>Managed IT Solutions</li><li>Remote Diagnostic And Support</li><li>IT Infrastructure Design and Installation</li></ul></div>
  <div class="fcol fc3 abs"><h4>Contact Informatiom</h4>
    <ul>
      <li><svg width="12" height="14" viewBox="0 0 12 14"><path d="M6 14S1 8 1 5a5 5 0 0 1 10 0c0 3-5 9-5 9z" fill="#f0862e"/><circle cx="6" cy="5" r="2" fill="#232228"/></svg><span>Address: Line goes here,<br>city name country name</span></li>
      <li><svg width="12" height="14" viewBox="0 0 12 14"><path d="M2 1h3l1 3-2 1c1 2 2 3 4 4l1-2 3 1v3c-6 1-11-4-10-10z" fill="#f0862e"/></svg><span>Phone: 123 456 7890</span></li>
      <li><svg width="12" height="14" viewBox="0 0 12 14"><rect x="0" y="3" width="12" height="8" fill="#f0862e"/><path d="M0 3l6 4 6-4" stroke="#232228" fill="none"/></svg><span>Email: info@example.com</span></li>
    </ul></div>
  <p class="copyright abs">Copyright © 2017 - Velmarketa Group, Inc - All rights reserved</p>
  <svg class="to-top abs" width="34" height="34" viewBox="0 0 34 34"><path d="M12 19l5-5 5 5" stroke="#fff" stroke-width="2" fill="none"/></svg>
</footer>

</body>
</html>
```